Modernization of existing web site

Update existing web site to a professional look vs a home-made site. Site look and navigation should be up to today's standards and display properly on mobile devices.
Only simple HTML and CSS is to be used as this is a basic site. No content management.
Existing site is https://www.plexumar.example

Target Market(s)

Insurance and Technology

Industry/Entity Type

Insurance and technology

Coding

Coded - Design and coding required

Number of Pages Required

5+ page

Font styles to use
Sans Serif

Colors
0054AA
0677BA
7BADD7
CADEEF
E8F1F8
0094D4
00A9DD
6FCCEA
C7EBF8
E9F6FB

Requirements
Must have
• A sleek, modern feel and also done with a button-downed industry in mind.
Nice to have
• Clean integration of the logo and name
Should not have
• Open to ideas

```html
<!DOCTYPE html>
<html lang="en">
<head>
<meta charset="utf-8">
<title>Plexumar</title>
<link href="https://fonts.googleapis.com/css2?family=Inter:wght@400;500;600;700&display=swap" rel="stylesheet">
<style>
:root{
  --brand:#0054AA;
  --band:#2779BE;
  --ink:#1a1a1a;
  --pale:#E8F1F8;
  --light:#CADEEF;
  --white:#ffffff;
  --black:#000000;
}
*{box-sizing:border-box;margin:0;padding:0}
html,body{width:814px;height:1200px;overflow:hidden}
body{position:relative;font-family:'Inter',sans-serif;color:var(--ink);background:var(--white)}
.abs{position:absolute}
.topbar{left:0;top:0;width:814px;height:33px;background:var(--band);color:var(--white);font-size:9px;display:flex;justify-content:flex-end;align-items:center;gap:14px;padding-right:62px}
.topbar span{display:flex;align-items:center;gap:4px}
.topbar svg{width:10px;height:10px;fill:none;stroke:var(--white);stroke-width:1.6}
.header{left:0;top:33px;width:814px;height:65px;background:var(--white)}
.brand{left:63px;top:21px;display:flex;align-items:center;gap:6px;font-size:22px;font-weight:700;color:var(--band);letter-spacing:.5px}
.brand i{width:20px;height:20px;border-radius:50%;background:var(--brand);display:block}
.nav{left:287px;top:27px;display:flex;gap:15px;font-size:11.5px;letter-spacing:.2px}
.nav a{color:var(--ink);text-decoration:none}
.btn{display:flex;align-items:center;justify-content:center;width:108px;height:29px;border-radius:4px;background:var(--brand);color:var(--white);font-size:10.5px;font-weight:600;text-decoration:none}
.btn.light{background:var(--white);color:var(--brand)}
.quote{left:643px;top:20px}
.hero{left:0;top:98px;width:814px;height:369px;background:linear-gradient(100deg,#3a5f84 0%,#4f7190 40%,#6f8ea8 70%,#8aa6bb 100%)}
.hero-copy{left:108px;top:131px;color:var(--white)}
.hero-copy .kicker{font-size:13.5px;font-weight:400}
.hero-copy h1{margin-top:14px;font-size:36px;line-height:38.5px;font-weight:600;letter-spacing:-.2px}
.hero-copy .btn{margin-top:15px}
.about{left:99px;top:432px;width:616px;height:272px;background:var(--white);box-shadow:0 8px 22px rgba(0,0,0,.14)}
.about-photo{left:0;top:0;width:282px;height:272px;background:linear-gradient(135deg,#d9c6a6 0%,#6b7585 45%,#3a4252 100%)}
.about-text{left:312px;top:45px;width:275px;font-size:10.5px;line-height:12.6px}
.about-text p{margin-bottom:12px}
.about-text .btn{margin-top:13px}
.services{left:0;top:747px;width:814px;height:324px;background:var(--band)}
.services h2{position:absolute;left:0;width:792px;top:38px;text-align:center;font-size:21px;font-weight:600;color:var(--pale)}
.svc{position:absolute;display:flex;align-items:center;gap:7px;color:var(--white);font-size:14px;line-height:14px}
.svc .icon{width:46px;height:46px;background:var(--pale);display:flex;align-items:center;justify-content:center;flex:none}
.svc svg{width:32px;height:32px;fill:none;stroke:var(--brand);stroke-width:1.5;stroke-linecap:round;stroke-linejoin:round}
.more-svc{left:353px;top:270px}
.footer{left:0;top:1071px;width:814px;height:129px;background:var(--black);color:var(--white);font-size:10.5px}
.f-links{left:105px;top:22px;line-height:17px}
.f-policy{left:225px;top:26px}
.f-contact{left:366px;top:29px;font-size:9.5px;line-height:17px}
.f-contact div{display:flex;align-items:center;gap:5px}
.f-contact svg{width:10px;height:10px;fill:none;stroke:var(--white);stroke-width:1.6}
.copy{left:607px;top:71px;font-size:9.5px;font-weight:600}
</style>
</head>
<body>
<div class="abs topbar">
  <span><svg viewBox="0 0 12 12"><path d="M2 1h2.5l1 3-1.5 1a6 6 0 0 0 3 3l1-1.5 3 1V10a1 1 0 0 1-1 1A9 9 0 0 1 1 2a1 1 0 0 1 1-1z"/></svg>555-014-2290</span>
  <span><svg viewBox="0 0 12 12"><rect x="1" y="2.5" width="10" height="7"/><path d="M1 2.5l5 4 5-4"/></svg>info@plexumar.example</span>
  <span><svg viewBox="0 0 12 12"><path d="M2 1h2.5l1 3-1.5 1a6 6 0 0 0 3 3l1-1.5 3 1V10a1 1 0 0 1-1 1A9 9 0 0 1 1 2a1 1 0 0 1 1-1z"/></svg>42 Willow Crest Ln&nbsp; Ridgeview, NV 89000</span>
</div>

<header class="abs header">
  <div class="abs brand"><i></i>PLEXUMAR</div>
  <nav class="abs nav"><a href="#">HOME</a><a href="#">OUR SERVICES</a><a href="#">ABOUT US</a><a href="#" style="margin-left:3px">CONTACT US</a></nav>
  <a class="abs btn quote" href="#">Request Quote</a>
</header>

<section class="abs hero" role="img" aria-label="Businessman holding a smartphone with a glowing digital globe and data graphics"></section>
<div class="abs hero-copy">
  <div class="kicker">Welcome to Plexumar</div>
  <h1>Navigating<br>Business and<br>Technology to<br>Generate Result</h1>
  <a class="btn" href="#">Get Started</a>
</div>

<section class="abs about">
  <div class="abs about-photo" role="img" aria-label="Two businessmen in suits reviewing a clipboard in an office"></div>
  <div class="abs about-text">
    <p>At PLEXUMAR, we are here to assist you in realizing your vision for your business.</p>
    <p>We offer a number of different services for insurance, technology, and financial services firms.</p>
    <p>We have extensive experience in many areas of business and technology combined with a deep level of integrity in the way we do business.</p>
    <p>If you have a specific need not mentioned on our website, contact us today with your details.</p>
    <a class="btn" href="#">More about us</a>
  </div>
</section>

<section class="abs services">
  <h2>Our Services</h2>
  <div class="svc" style="left:98px;top:97px"><div class="icon"><svg viewBox="0 0 32 32"><circle cx="14" cy="16" r="8"/><circle cx="14" cy="16" r="3"/><path d="M22 12h6M22 20h6M22 16h4"/></svg></div>Business and<br>Technology Strategy</div>
  <div class="svc" style="left:306px;top:97px"><div class="icon"><svg viewBox="0 0 32 32"><rect x="5" y="12" width="22" height="14"/><path d="M9 6v6M16 6v6M23 6v6M3 26h26"/><circle cx="16" cy="20" r="3"/></svg></div>Distribution Channel<br>Development</div>
  <div class="svc" style="left:514px;top:100px"><div class="icon"><svg viewBox="0 0 32 32"><rect x="6" y="5" width="16" height="22"/><path d="M9 17h10M9 21h8"/><path d="M20 16l6 2v4c0 3-3 5-6 6-3-1-6-3-6-6v-4z"/></svg></div>Data/Reporting/<br>Analitycs</div>
  <div class="svc" style="left:98px;top:172px"><div class="icon"><svg viewBox="0 0 32 32"><path d="M16 4l8 3v6c0 5-4 8-8 10-4-2-8-5-8-10V7z"/><path d="M12 13l3 3 5-5"/><path d="M4 18l4 8h6M28 18l-4 8h-6"/></svg></div>Insurance Operation<br>/Process</div>
  <div class="svc" style="left:306px;top:172px"><div class="icon"><svg viewBox="0 0 32 32"><circle cx="13" cy="14" r="8"/><circle cx="18" cy="18" r="5"/><path d="M22 22l6 6"/></svg></div>M/A Due Diligence</div>
  <div class="svc" style="left:514px;top:175px"><div class="icon"><svg viewBox="0 0 32 32"><circle cx="15" cy="11" r="7"/><circle cx="15" cy="11" r="3"/><path d="M15 11v14l-3-3M15 17h6v8"/></svg></div>Technology<br>Implementation</div>
  <a class="abs btn light more-svc" href="#">More services</a>
</section>

<footer class="abs footer">
  <div class="abs f-links">Home<br>Our Services<br>About Us<br>Contact Us</div>
  <div class="abs f-policy">Privacy Policy</div>
  <div class="abs f-contact">
    <div><svg viewBox="0 0 12 12"><path d="M6 11s4-4 4-6.5a4 4 0 0 0-8 0C2 7 6 11 6 11z"/><circle cx="6" cy="4.5" r="1.3"/></svg>42 Willow Crest Ln&nbsp; Ridgeview, NV 89000</div>
    <div><svg viewBox="0 0 12 12"><rect x="1" y="2.5" width="10" height="7"/><path d="M1 2.5l5 4 5-4"/></svg>info@plexumar.example</div>
    <div style="margin-top:2px"><svg viewBox="0 0 12 12"><path d="M2 1h2.5l1 3-1.5 1a6 6 0 0 0 3 3l1-1.5 3 1V10a1 1 0 0 1-1 1A9 9 0 0 1 1 2a1 1 0 0 1 1-1z"/></svg>555-014-2290</div>
  </div>
  <div class="abs copy">©2022 Plexumar LLC</div>
</footer>
</body>
</html>
```